Business cards for the RT Group

We are looking for a template for our new business cards for our company that we can edit ourselves.
You will find our company colors in the logo. the logo on the back and on the front
first name Last Name
position
E-mail address
mobile number
landline number
Companies we have 2 RT Sicherheit GmbH and RT Services GmbH
address
Lindauer Weg 42
22543 Hamburg
www.rtverbund-beispiel.de

Something modern, simple but professional

if you have any questions, bring it on.

Industry/Entity Type

Sicherheit

Contact Information for Business Card

Steht in der Beschreibung

Colors
F0912C
F2A743
F7CA91
FBE8D2
FDF5EE

Requirements
Must have
• recognition value
Nice to have
• professional
Should not have
• Playful

```html
<!DOCTYPE html>
<html lang="de">
<head>
<meta charset="utf-8">
<title>RT Gruppe – Visitenkarten</title>
<link href="https://fonts.googleapis.com/css2?family=Roboto:wght@400;500;700&display=swap" rel="stylesheet">
<style>
  :root {
    --stage: #ebebed;
    --card-white: #ffffff;
    --brand-orange: #f47f22;
    --brand-grey: #5b5b5d;
    --text-grey: #555558;
    --title-blue: #4d5a86;
    --rule: #3c3c3e;
  }
  * { box-sizing: border-box; margin: 0; padding: 0; }
  html, body {
    width: 1200px; height: 1000px; overflow: hidden;
    background: var(--stage);
    font-family: "Roboto", Arial, sans-serif;
  }
  .stage { position: relative; width: 1200px; height: 1000px; }
  .card {
    position: absolute; top: 214px;
    width: 335px; height: 585px;
    text-align: center;
  }
  .card--front { left: 245px; background: var(--card-white); }
  .card--back { left: 642px; background: var(--brand-orange); }

  .wordmark {
    position: absolute; left: 0; right: 0;
    display: flex; align-items: center; justify-content: center; gap: 10px;
  }
  .wordmark__dot { width: 22px; height: 22px; border-radius: 50%; background: var(--brand-orange); }
  .wordmark__name {
    font-weight: 700; font-size: 40px; letter-spacing: 1px;
    color: var(--brand-grey); line-height: 1;
  }
  .card--front .wordmark { top: 112px; }
  .card--back .wordmark { top: 242px; }
  .card--back .wordmark__dot { background: var(--brand-grey); }

  .person { position: absolute; top: 250px; left: 0; right: 0; }
  .person__name {
    font-weight: 700; font-size: 22px; color: var(--brand-orange);
    letter-spacing: 0.3px; line-height: 26px;
  }
  .person__role {
    font-size: 15px; color: var(--title-blue);
    letter-spacing: 1.6px; margin-top: 2px;
  }

  .divider {
    position: absolute; top: 331px; left: 68px; width: 200px; height: 22px;
    display: flex; align-items: center; justify-content: center; gap: 11px;
  }
  .divider__line { flex: 1; height: 2px; background: linear-gradient(90deg, transparent, var(--rule)); }
  .divider__line--right { background: linear-gradient(90deg, var(--rule), transparent); }
  .divider__icon { width: 19px; height: 19px; display: block; }

  .contact {
    position: absolute; top: 383px; left: 0; right: 0;
    font-size: 16px; line-height: 23.5px; color: var(--text-grey);
  }
  .address {
    position: absolute; top: 486px; left: 0; right: 0;
    font-size: 16px; line-height: 23.5px; color: var(--brand-orange);
  }
  .companies {
    position: absolute; top: 499px; left: 0; right: 0;
    font-size: 16px; line-height: 23.5px; color: var(--card-white);
  }
</style>
</head>
<body>
<main class="stage">

  <section class="card card--front" aria-label="Vorderseite">
    <div class="wordmark">
      <span class="wordmark__dot"></span>
      <span class="wordmark__name">RT GRUPPE</span>
    </div>

    <div class="person">
      <p class="person__name">JOHNATHAN DOE</p>
      <p class="person__role">DIRECTOR</p>
    </div>

    <div class="divider">
      <span class="divider__line"></span>
      <svg class="divider__icon" viewBox="0 0 20 20" aria-label="Telefon">
        <circle cx="10" cy="10" r="10" fill="var(--rule)"/>
        <path d="M7 5.2c.4-.3.9-.2 1.1.2l.9 1.7c.2.4.1.8-.2 1.1l-.6.5c.5 1.1 1.4 2 2.5 2.5l.5-.6c.3-.3.7-.4 1.1-.2l1.7.9c.4.2.5.7.2 1.1l-.8 1c-.4.5-1.1.6-1.7.4-2.6-1-4.6-3-5.6-5.6-.2-.6-.1-1.3.4-1.7z" fill="#fff"/>
      </svg>
      <svg class="divider__icon" viewBox="0 0 20 20" aria-label="E-Mail">
        <circle cx="10" cy="10" r="10" fill="var(--rule)"/>
        <rect x="5" y="6.5" width="10" height="7" rx="1" fill="#fff"/>
        <path d="M5.3 7l4.7 3.6L14.7 7" fill="none" stroke="var(--rule)" stroke-width="1"/>
      </svg>
      <svg class="divider__icon" viewBox="0 0 20 20" aria-label="Web">
        <circle cx="10" cy="10" r="10" fill="var(--rule)"/>
        <g fill="none" stroke="#fff" stroke-width="1">
          <circle cx="10" cy="10" r="5.5"/>
          <ellipse cx="10" cy="10" rx="2.4" ry="5.5"/>
          <path d="M4.5 10h11M5.3 7.3h9.4M5.3 12.7h9.4"/>
        </g>
      </svg>
      <span class="divider__line divider__line--right"></span>
    </div>

    <address class="contact" style="font-style:normal">
      <p>123 456 7890</p>
      <p>email@rtverbund-beispiel.de</p>
      <p>www.rtverbund-beispiel.de</p>
    </address>

    <address class="address" style="font-style:normal">
      <p>Lindauer Weg 42</p>
      <p>22543 Hamburg</p>
    </address>
  </section>

  <section class="card card--back" aria-label="Rückseite">
    <div class="wordmark">
      <span class="wordmark__dot"></span>
      <span class="wordmark__name">RT GRUPPE</span>
    </div>
    <div class="companies">
      <p>RT Sicherheit GmbH</p>
      <p>RT Services GmbH</p>
    </div>
  </section>

</main>
</body>
</html>
```